Online Certificate in Research Methods needs a Digital Banner ad

We are launching an online graduate certificate in Quantitative and Qualitative Social Science Research Methods. We need a digital banner created so we can advertise on pagenook, seekora, and some other places.

The banner needs to use these color schemes and fonts: https://universityrelations.bmlu.edu/brand-guide/color

Would like the banner to say (either as three lines, or if not in three lines, have these sets of words at minimum on the same line):
Online Graduate Certificate in
Quantitative & Qualitative
Social Science Research Methods

We also want it to say Brennmoor Lake University and Next Start Date August 18, 2021. I’ve attached a picture of a version we tried to create but is hard to read.

We need a graphic that looks good in the following specs:
600px wide x 70px tall, high quality (at least 300 dpi) jpg or png

And
Pagenook recommendations:
Design Recommendations
• File Type: JPG or PNG
• Ratio: 1.91:1 to 1:1
• Resolution: At least 1080 x 1080 pixels
Text Recommendations
• Primary Text: 125 characters
• Headline: 40 characters
• Description: 30 characters
Technical Requirements
• Maximum File Size: 30MB
• Minimum Width: 600 pixels
• Minimum Height: 600 pixels
• Aspect Ratio Tolerance: 3%

```html
<!DOCTYPE html>
<html lang="en">
<head>
<meta charset="utf-8">
<title>Online Graduate Certificate Banner – Draft and Details</title>
<link rel="stylesheet" href="https://fonts.googleapis.com/css2?family=Arimo:wght@700&family=Roboto+Condensed:ital,wght@0,400;0,700;1,700&display=swap">
<style>
  :root {
    --navy: #002855;
    --navy-light: #1d3f6d;
    --gold: #eaaa00;
    --gold-bright: #f3bd1e;
    --gold-glow: #fff4cf;
    --label-light: #d2d2d2;
    --label-dark: #3b3b3b;
    --stage-grey: #d9d9d9;
    --white: #ffffff;
    --photo-cool: #6f7f95;
    --photo-warm: #b59a5c;
  }
  * { margin: 0; padding: 0; box-sizing: border-box; }
  html, body { width: 1200px; height: 1000px; overflow: hidden; background: var(--white); }
  body { position: relative; font-family: "Roboto Condensed", "Arial Narrow", sans-serif; }

  .section-label {
    position: absolute; left: 0; width: 1200px; text-align: center;
    font-weight: 700; font-size: 34px; letter-spacing: 0.5px; line-height: 1;
  }
  .section-label--draft { top: 23px; color: var(--label-light); }
  .section-label--details { top: 248px; color: var(--label-dark); }

  .details-stage { position: absolute; left: 0; top: 285px; width: 1200px; height: 715px; background: var(--stage-grey); }
  .details-pointer { position: absolute; left: 580px; top: 0; }

  /* shared pieces */
  .photo-area { position: absolute; }
  .cta-button {
    position: absolute; display: flex; align-items: center;
    background: linear-gradient(180deg, #0b3a72 0%, var(--navy) 55%, #001d40 100%);
    border-radius: 999px; color: var(--white); font-family: "Arimo", Arial, sans-serif; font-weight: 700;
    box-shadow: 0 0 0 3px rgba(0,40,85,0.35), 0 3px 8px rgba(0,0,0,0.35);
  }
  .cta-button__text { display: flex; flex-direction: column; line-height: 1.0; }
  .brand-name { position: absolute; display: flex; align-items: center; color: var(--navy); font-weight: 400; white-space: nowrap; }
  .brand-name__mark { background: var(--gold); display: inline-block; }
  .headline { position: absolute; text-align: center; color: var(--white); font-weight: 700; text-transform: uppercase; }
  .headline__date { color: var(--gold); font-style: italic; }

  /* draft banner */
  .banner-draft { position: absolute; left: 45px; top: 74px; width: 1110px; height: 130px; background: var(--navy); overflow: hidden; }
  .banner-draft .gold-field { position: absolute; left: 820px; top: 0; width: 290px; height: 130px;
    background: radial-gradient(ellipse 140px 40px at 190px 110px, var(--gold-glow), var(--gold-bright) 70%, var(--gold)); }
  .banner-draft .photo-area { left: 545px; top: 0; width: 330px; height: 130px;
    clip-path: polygon(20px 0, 100% 0, 100% 100%, 55px 100%, 0 50%);
    background: linear-gradient(90deg, var(--photo-cool) 0%, var(--photo-warm) 55%, var(--gold-bright) 100%); }
  .banner-draft .headline { left: 110px; top: 18px; width: 416px; font-size: 24.5px; line-height: 24px; }
  .banner-draft .headline__date { display: block; font-size: 18px; line-height: 26px; }
  .banner-draft .cta-button { left: 886px; top: 16px; width: 178px; height: 56px; padding-left: 30px; gap: 10px; }
  .banner-draft .cta-button__small { font-size: 12px; }
  .banner-draft .cta-button__large { font-size: 18px; }
  .banner-draft .brand-name { left: 898px; top: 92px; font-size: 15px; gap: 6px; }
  .banner-draft .brand-name__mark { width: 12px; height: 12px; }

  /* detail: right side */
  .detail-cta { position: absolute; left: 0; top: 372px; width: 1155px; height: 273px; overflow: hidden;
    background: radial-gradient(ellipse 330px 70px at 880px 240px, var(--gold-glow), var(--gold-bright) 65%, var(--gold)); }
  .detail-cta .photo-area { left: 0; top: 0; width: 640px; height: 273px;
    background: linear-gradient(90deg, var(--photo-cool) 0%, #8c8a82 30%, var(--photo-warm) 60%, rgba(243,189,30,0) 100%); }
  .detail-cta .corner { position: absolute; left: 0; top: 0; }
  .detail-cta .cta-button { left: 685px; top: 40px; width: 370px; height: 113px; padding-left: 62px; gap: 20px; }
  .detail-cta .cta-button__small { font-size: 25px; }
  .detail-cta .cta-button__large { font-size: 37px; }
  .detail-cta .brand-name { left: 705px; top: 196px; font-size: 33px; gap: 12px; }
  .detail-cta .brand-name__mark { width: 26px; height: 26px; }

  /* detail: left side */
  .detail-headline { position: absolute; left: 64px; top: 683px; width: 1136px; height: 274px; background: var(--navy); overflow: hidden; }
  .detail-headline .accent { position: absolute; left: 0; top: 0; }
  .detail-headline .headline { left: 200px; top: 38px; width: 906px; font-size: 53px; line-height: 49.5px; }
  .detail-headline .headline__date { display: block; font-size: 40px; line-height: 56px; }
</style>
</head>
<body>

  <div class="section-label section-label--draft">DRAFT DESIGN</div>

  <div class="banner-draft">
    <svg class="accent" width="140" height="130" viewBox="0 0 140 130" style="position:absolute;left:0;top:0">
      <polygon points="0,0 42,0 20,60 70,130 0,130" fill="var(--navy-light)"/>
      <polygon points="0,72 0,90 38,130 60,130" fill="var(--gold)"/>
    </svg>
    <div class="gold-field"></div>
    <div class="photo-area" role="img" aria-label="Photo of students working on laptops in a classroom"></div>
    <h1 class="headline">Online Graduate Certificate in<br>Quantitative &amp; Qualitative<br>Social Science Research Methods
      <span class="headline__date">Next Start Date August 18, 2021</span></h1>
    <div class="cta-button">
      <svg width="22" height="26" viewBox="0 0 22 26"><path d="M2 2 L10 13 L2 24 M11 2 L19 13 L11 24" fill="none" stroke="var(--white)" stroke-width="4" stroke-linejoin="round"/></svg>
      <span class="cta-button__text"><span class="cta-button__small">Click here for</span><span class="cta-button__large">More Info</span></span>
    </div>
    <div class="brand-name"><span class="brand-name__mark"></span>Brennmoor Lake University</div>
  </div>

  <div class="section-label section-label--details">DETAILS</div>

  <div class="details-stage">
    <svg class="details-pointer" width="40" height="26" viewBox="0 0 40 26"><polygon points="0,0 40,0 20,26" fill="var(--white)"/></svg>
  </div>

  <div class="detail-cta">
    <div class="photo-area" role="img" aria-label="Photo of students working on laptops in a classroom"></div>
    <svg class="corner" width="80" height="273" viewBox="0 0 80 273">
      <polygon points="0,190 62,273 0,273" fill="var(--navy-light)"/>
    </svg>
    <div class="cta-button">
      <svg width="44" height="52" viewBox="0 0 44 52"><path d="M4 4 L20 26 L4 48 M22 4 L38 26 L22 48" fill="none" stroke="var(--white)" stroke-width="8" stroke-linejoin="round"/></svg>
      <span class="cta-button__text"><span class="cta-button__small">Click here for</span><span class="cta-button__large">More Info</span></span>
    </div>
    <div class="brand-name"><span class="brand-name__mark"></span>Brennmoor Lake University</div>
  </div>

  <div class="detail-headline">
    <svg class="accent" width="260" height="274" viewBox="0 0 260 274">
      <polygon points="0,0 118,0 72,100 150,274 0,274" fill="var(--navy-light)"/>
      <polygon points="0,77 0,118 118,274 148,274" fill="var(--gold)"/>
    </svg>
    <h2 class="headline">Online Graduate Certificate in<br>Quantitative &amp; Qualitative<br>Social Science Research Methods
      <span class="headline__date">Next Start Date August 18, 2021</span></h2>
  </div>

</body>
</html>
```